Business card for massage therapy company called Brook Fern Wellness

Need business card for massage therapy company called Brook Fern Wellness. Would like my logo on the front and the back of the card I have 3 options of logos and you can play with what looks better.

Would like this information displayed on the back of the card:

Marcus Ellery
Licensed Massage Therapist
321-555-0147
brookfern-example.com
brookfern_rest_

```html
<!DOCTYPE html>
<html lang="en">
<head>
<meta charset="utf-8">
<title>Brook Fern Wellness – Business Card</title>
<link rel="stylesheet" href="https://fonts.googleapis.com/css2?family=Marcellus&family=Montserrat:wght@300;400&display=swap">
<style>
  :root {
    --sage: #6e7560;
    --sage-dark: #5f6652;
    --sage-text: #5c6350;
    --tan: #c7977a;
    --white: #ffffff;
    --backdrop: #e9e9e6;
  }
  * { box-sizing: border-box; margin: 0; padding: 0; }
  html, body { width: 1200px; height: 1015px; overflow: hidden; }
  body {
    background: var(--backdrop);
    font-family: "Montserrat", sans-serif;
    position: relative;
  }
  .card {
    position: absolute;
    left: 300px;
    width: 600px;
    height: 343px;
    overflow: hidden;
    box-shadow: 0 8px 24px rgba(0,0,0,0.18);
  }
  .card-front { top: 110px; background: var(--sage); }
  .card-back { top: 520px; background: var(--white); }

  .foliage {
    position: absolute;
    inset: 0;
    background:
      radial-gradient(ellipse 220px 160px at 88% 30%, rgba(90,98,78,0.55), transparent 70%),
      radial-gradient(ellipse 200px 150px at 12% 80%, rgba(90,98,78,0.5), transparent 70%);
  }
  .front-mark {
    position: absolute;
    inset: 0;
    display: flex;
    align-items: center;
    justify-content: center;
    gap: 16px;
  }
  .mark-dot {
    width: 18px; height: 18px;
    border: 2px solid var(--white);
    border-radius: 50%;
  }
  .front-name {
    font-family: "Marcellus", serif;
    font-size: 34px;
    letter-spacing: 3px;
    color: var(--white);
    text-transform: uppercase;
  }

  .back-wave { position: absolute; inset: 0; }
  .holder {
    position: absolute;
    left: 40px; top: 58px;
  }
  .holder-name {
    font-family: "Marcellus", serif;
    font-size: 22px;
    letter-spacing: 1px;
    color: var(--sage-text);
    text-transform: uppercase;
  }
  .holder-title {
    font-size: 15px;
    font-weight: 300;
    color: var(--tan);
    margin-top: 2px;
  }
  .back-brand {
    position: absolute;
    right: 36px; top: 50px;
    display: flex;
    align-items: center;
    gap: 12px;
  }
  .back-brand .mark-dot { border-color: var(--sage-text); }
  .back-brand-name {
    font-family: "Marcellus", serif;
    font-size: 24px;
    letter-spacing: 3px;
    color: var(--sage-text);
    text-transform: uppercase;
    text-align: center;
    line-height: 1.2;
  }
  .contacts {
    position: absolute;
    left: 40px; bottom: 30px;
    list-style: none;
    color: var(--white);
    font-size: 15px;
    font-weight: 400;
  }
  .contacts li {
    display: flex;
    align-items: center;
    gap: 10px;
    margin-top: 6px;
  }
  .contact-icon {
    width: 22px; height: 22px;
    border: 1.3px solid var(--white);
    border-radius: 50%;
    display: flex;
    align-items: center;
    justify-content: center;
  }
</style>
</head>
<body>

<section class="card card-front">
  <div class="foliage" role="img" aria-label="Faint leafy branch pattern across the card"></div>
  <div class="front-mark">
    <span class="mark-dot"></span>
    <span class="front-name">Brook Fern Wellness</span>
  </div>
</section>

<section class="card card-back">
  <svg class="back-wave" viewBox="0 0 600 343" width="600" height="343" aria-hidden="true">
    <path d="M0,222 Q330,222 600,118 L600,343 L0,343 Z" fill="var(--sage)"/>
    <path d="M0,232 Q335,232 600,130" fill="none" stroke="var(--white)" stroke-width="3"/>
  </svg>

  <div class="holder">
    <p class="holder-name">Marcus Ellery</p>
    <p class="holder-title">Licensed Massage Therapist</p>
  </div>

  <div class="back-brand">
    <span class="mark-dot"></span>
    <p class="back-brand-name">Brook Fern<br>Wellness</p>
  </div>

  <ul class="contacts">
    <li>
      <span class="contact-icon">
        <svg width="12" height="12" viewBox="0 0 24 24" aria-hidden="true"><path d="M6.6 10.8a15 15 0 0 0 6.6 6.6l2.2-2.2a1 1 0 0 1 1-.25 11 11 0 0 0 3.6.6 1 1 0 0 1 1 1V20a1 1 0 0 1-1 1A17 17 0 0 1 3 4a1 1 0 0 1 1-1h3.5a1 1 0 0 1 1 1c0 1.25.2 2.45.6 3.6a1 1 0 0 1-.25 1z" fill="var(--white)"/></svg>
      </span>
      321-555-0147
    </li>
    <li>
      <span class="contact-icon">
        <svg width="13" height="13" viewBox="0 0 24 24" aria-hidden="true" fill="none" stroke="var(--white)" stroke-width="1.8"><circle cx="12" cy="12" r="10"/><ellipse cx="12" cy="12" rx="4.5" ry="10"/><line x1="2" y1="12" x2="22" y2="12"/></svg>
      </span>
      brookfern-example.com
    </li>
    <li>
      <span class="contact-icon"></span>
      brookfern_rest_
    </li>
  </ul>
</section>

</body>
</html>
```